Independence Day Graphics for Sale

I want to create 10 social media graphics (new Pictora size 4:5 (1080 x 1350 pixels) focusing on our July 4th Sale Graphics, using any of the pics attached. Use the attached pics, NO RANDOM STOCK PHOTOGRAPHY. For the color scheme of the graphics, they should all be complementary to the product colors in the photos.
You can add any of the photos attached but none are required. You can do some of the graphics in all text. I mainly need BOLD text that says one of the headlines (10 total) SEE ATTACHED WORD DOCUMENT for the headlines to use.

Target Market(s)

women looking to lose weight

Requirements
Must have
• pics attached and text attached

```html
<!DOCTYPE html>
<html lang="en">
<head>
<meta charset="utf-8">
<title>July 4th Sale Social Set</title>
<link href="https://fonts.googleapis.com/css2?family=Antonio:wght@300;400&family=Bebas+Neue&display=swap" rel="stylesheet">
<style>
:root{
  --canvas:#c3c4c7;
  --navy:#3a2b78;
  --plum:#6a2d6e;
  --red:#ee3a43;
  --white:#ffffff;
  --paper:#f2f2f4;
  --paper-dark:#e2e2e6;
}
*{margin:0;padding:0;box-sizing:border-box}
html,body{width:1200px;height:609px;overflow:hidden;background:var(--canvas)}
body{position:relative;font-family:"Bebas Neue",sans-serif}
.tile{position:absolute;width:226px;height:283px;overflow:hidden}
.row-1{top:17px}.row-2{top:308px}
.col-1{left:17px}.col-2{left:252px}.col-3{left:487px}.col-4{left:722px}.col-5{left:957px}
.bg-brand{background:linear-gradient(160deg,var(--navy) 0%,var(--plum) 55%,var(--red) 100%)}
.bg-paper{background:linear-gradient(180deg,var(--paper-dark) 0%,var(--paper) 55%,#fafafa 100%)}
.photo{position:absolute;background:linear-gradient(180deg,rgba(110,70,60,.55) 0%,rgba(200,160,140,.45) 30%,rgba(240,236,234,.6) 55%,rgba(40,30,50,.55) 78%,rgba(225,220,216,.6) 100%)}
.bottles{position:absolute;border-radius:6px 6px 2px 2px;background:linear-gradient(180deg,#f7f7f8 0%,#e9e9ee 55%,#d7cde0 80%,#e9e3ea 100%)}
.abs{position:absolute}
.t{position:absolute;line-height:1;white-space:nowrap}
.light{font-family:"Antonio",sans-serif;font-weight:300}
.regular{font-family:"Antonio",sans-serif;font-weight:400}
.white{color:var(--white)}.red{color:var(--red)}.navy{color:var(--navy)}
.pct{font-size:.5em;vertical-align:top;line-height:1.3}
.center{text-align:center}
.up{transform-origin:0 0;transform:rotate(-90deg)}
</style>
</head>
<body>

<!-- July 4th Mega Sale -->
<section class="tile row-1 col-1 bg-brand">
  <div class="photo" style="left:100px;top:0;width:126px;height:283px" role="img" aria-label="Smiling woman in white top with supplement bottles on a kitchen counter"></div>
  <div class="t white" style="left:16px;top:14px;font-size:30px">July 4th</div>
  <div class="t white" style="left:15px;top:41px;font-size:50px">Mega</div>
  <div class="t white" style="left:15px;top:83px;font-size:49px">Sale!</div>
  <div class="abs" style="left:17px;top:152px;width:80px;height:90px;border:1.5px solid var(--white)"></div>
  <div class="t white center" style="left:17px;width:80px;top:152px;font-size:50px">25%</div>
  <div class="t white center" style="left:17px;width:80px;top:193px;font-size:54px;letter-spacing:5px;text-indent:5px">Off</div>
  <div class="abs" style="left:17px;top:242px;width:80px;height:24px;background:var(--white)"></div>
  <div class="t navy regular center" style="left:17px;width:80px;top:243px;font-size:19px">EVERYTHING</div>
</section>

<!-- Biggest 4th of July Sale Ever -->
<section class="tile row-1 col-2 bg-paper">
  <div class="t red" style="left:26px;top:12px;font-size:35px">Biggest</div>
  <div class="t navy light" style="left:27px;top:37px;font-size:23px">4TH OF JULY</div>
  <div class="t red" style="left:26px;top:62px;font-size:39px">Sale</div>
  <div class="t red" style="left:26px;top:94px;font-size:40px">Ever!</div>
  <div class="abs" style="left:121px;top:16px;width:77px;height:110px;border:2px solid var(--navy)"></div>
  <div class="t navy center" style="left:121px;width:77px;top:17px;font-size:48px">25%</div>
  <div class="t navy center" style="left:121px;width:77px;top:57px;font-size:49px;letter-spacing:6px;text-indent:6px">Off</div>
  <div class="abs" style="left:121px;top:103px;width:77px;height:23px;background:var(--navy)"></div>
  <div class="t white center" style="left:121px;width:77px;top:105px;font-size:19px;letter-spacing:2px;text-indent:2px">Sitewide</div>
  <div class="bottles" style="left:28px;top:158px;width:170px;height:96px" role="img" aria-label="Four supplement bottles in a row"></div>
</section>

<!-- Historic 4th of July Sale -->
<section class="tile row-1 col-3" style="background:linear-gradient(165deg,#f0f0f2 0%,var(--red) 22%,var(--plum) 60%,var(--navy) 100%)">
  <div class="photo" style="left:119px;top:0;width:107px;height:283px" role="img" aria-label="Smiling woman holding a supplement bottle"></div>
  <div class="t navy regular" style="left:15px;top:11px;font-size:29px">HISTORIC</div>
  <div class="t navy" style="left:15px;top:38px;font-size:21px">4th of July</div>
  <div class="t white up" style="left:5px;top:218px;font-size:100px">Sale!</div>
  <div class="abs" style="left:16px;top:225px;width:69px;height:42px;border:1px solid var(--white)"></div>
  <div class="t white center" style="left:16px;width:69px;top:226px;font-size:30px">25<span class="pct">%</span> Off</div>
  <div class="t white light center" style="left:16px;width:69px;top:251px;font-size:13px">OF EVERYTHING</div>
</section>

<!-- Mega Summer Blowout -->
<section class="tile row-1 col-4 bg-paper">
  <div class="t red center" style="left:0;width:226px;top:13px;font-size:32px">Mega Summer</div>
  <div class="t center" style="left:0;width:226px;top:41px;font-size:68px;color:var(--white);-webkit-text-stroke:1.5px var(--red);text-shadow:2px 2px 0 var(--navy)">Blowout!</div>
  <svg class="abs" style="left:44px;top:108px" width="138" height="57" viewBox="0 0 138 57" aria-hidden="true">
    <path d="M7 1H1V56H7M131 1H137V56H131" fill="none" stroke="var(--navy)" stroke-width="1.2"/>
  </svg>
  <div class="t navy center" style="left:44px;width:138px;top:101px;font-size:51px">25<span class="pct">%</span> Off</div>
  <div class="t navy center" style="left:44px;width:138px;top:144px;font-size:28px">Of Everything</div>
  <div class="bottles" style="left:13px;top:184px;width:202px;height:83px" role="img" aria-label="Four supplement bottles in a row"></div>
</section>

<!-- One-time only -->
<section class="tile row-1 col-5 bg-brand">
  <div class="photo" style="left:95px;top:0;width:131px;height:283px" role="img" aria-label="Smiling woman behind a row of supplement bottles and skincare products"></div>
  <div class="abs" style="left:17px;top:17px;width:68px;height:44px;background:var(--red)"></div>
  <div class="t white" style="left:21px;top:19px;font-size:24px">One-Time</div>
  <div class="t white" style="left:21px;top:39px;font-size:24px">Only:</div>
  <div class="t white up" style="left:10px;top:206px;font-size:63px">25<span class="pct">%</span> Off</div>
  <div class="t white light up" style="left:58px;top:206px;font-size:31px">OF EVERYTHING</div>
</section>

<!-- Stock-up event -->
<section class="tile row-2 col-1 bg-paper">
  <div class="t red" style="left:47px;top:12px;font-size:60px">25<span class="pct">%</span> Off</div>
  <div class="t red" style="left:47px;top:64px;font-size:28px;letter-spacing:-.6px">Stock-Up Event:</div>
  <div class="abs" style="left:47px;top:91px;width:134px;height:2px;background:var(--navy)"></div>
  <div class="t navy" style="left:47px;top:91px;font-size:60px">25<span class="pct">%</span> Off</div>
  <div class="t navy" style="left:47px;top:145px;font-size:28px;letter-spacing:-.6px">Stock-Up Event:</div>
  <div class="bottles" style="left:14px;top:186px;width:200px;height:83px" role="img" aria-label="Four supplement bottles in a row"></div>
</section>

<!-- Lowest prices -->
<section class="tile row-2 col-2" style="background:linear-gradient(155deg,#6b3a8a 0%,#c23a5e 45%,var(--red) 100%)">
  <div class="photo" style="left:0;top:0;width:226px;height:283px;opacity:.55" role="img" aria-label="Woman standing behind a counter of supplement bottles and skincare products"></div>
  <div class="t white center" style="left:0;width:226px;top:76px;font-size:31px;letter-spacing:-.8px">The Lowest Prices</div>
  <div class="t white center" style="left:0;width:226px;top:102px;font-size:31px;letter-spacing:-.8px">We've Ever Offered!</div>
  <div class="abs" style="left:47px;top:132px;width:133px;height:51px;border:1px solid var(--white)"></div>
  <div class="t white center" style="left:47px;width:133px;top:132px;font-size:57px">25<span class="pct">%</span> Off</div>
</section>

<!-- Our biggest discount ever -->
<section class="tile row-2 col-3" style="background:linear-gradient(180deg,var(--navy) 0%,var(--plum) 35%,var(--red) 80%)">
  <div class="photo" style="left:112px;top:60px;width:114px;height:223px" role="img" aria-label="Smiling woman holding a supplement bottle"></div>
  <div class="t white" style="left:15px;top:14px;font-size:40px;letter-spacing:-1px">Our Biggest</div>
  <div class="t white" style="left:15px;top:47px;font-size:40px;letter-spacing:-.5px">Discount</div>
  <div class="t white" style="left:15px;top:81px;font-size:40px">Ever!</div>
  <div class="t white" style="left:15px;top:116px;font-size:45px">25%</div>
  <div class="t white" style="left:15px;top:157px;font-size:48px;letter-spacing:6px">Off</div>
  <svg class="abs" style="left:16px;top:198px" width="63" height="12" viewBox="0 0 63 12" aria-hidden="true">
    <path d="M0 6H25M38 6H63" stroke="var(--white)" stroke-width="1"/>
  </svg>
  <div class="t white center" style="left:16px;width:63px;top:198px;font-size:12px">Of</div>
  <div class="t white" style="left:15px;top:210px;font-size:37px;letter-spacing:-.5px">Every</div>
  <div class="t white" style="left:15px;top:239px;font-size:37px;letter-spacing:-.5px">Thing</div>
</section>

<!-- Don't wait -->
<section class="tile row-2 col-4 bg-paper">
  <div class="t red" style="left:17px;top:11px;font-size:63px">Don't</div>
  <div class="t red" style="left:17px;top:65px;font-size:64px">Wait!</div>
  <div class="abs" style="left:137px;top:18px;width:1.5px;height:100px;background:var(--red)"></div>
  <div class="t navy" style="left:149px;top:13px;font-size:46px;letter-spacing:2px">25<span class="pct">%</span></div>
  <div class="t navy" style="left:148px;top:52px;font-size:48px">Off</div>
  <div class="abs" style="left:146px;top:98px;width:64px;height:20px;background:var(--navy)"></div>
  <div class="t white center" style="left:146px;width:64px;top:100px;font-size:17px">Ends Soon</div>
  <div class="bottles" style="left:14px;top:151px;width:196px;height:111px" role="img" aria-label="Four supplement bottles in a row"></div>
</section>

<!-- Last chance -->
<section class="tile row-2 col-5" style="background:linear-gradient(135deg,var(--navy) 0%,var(--plum) 50%,var(--red) 100%)">
  <div class="photo" style="left:120px;top:78px;width:106px;height:205px" role="img" aria-label="Smiling woman holding a supplement bottle"></div>
  <div class="t white" style="left:17px;top:25px;font-size:43px">Last</div>
  <div class="t white" style="left:17px;top:65px;font-size:43px">Chance</div>
  <div class="t white" style="left:17px;top:104px;font-size:43px">25<span class="pct">%</span> Off</div>
  <div class="t white" style="left:17px;top:143px;font-size:43px">Time Is</div>
  <div class="t white" style="left:17px;top:180px;font-size:43px;letter-spacing:-.5px">Running</div>
  <div class="t white" style="left:17px;top:220px;font-size:43px">Out!</div>
</section>

</body>
</html>
```